New website for a personal transformation academy

We need a website with a landing page and five sub-pages and either pages under each or one page where it is possible to jump between sections. The site will need to have a choice between two languages (English & Icelandic).
Needed functionality is:
Landing page with a link to social media posts, mail list registration, Facebook messenger option and testimonies
1. Brindmoor Academy information with an option to add videos and registration sheet, see details attached
2. Vireltones, see details attached
3. Personal vireltones, information and order sheet
4. From Metatron, informational text
5. About us, CV with the option of adding video
Further details in the attached picture.
Brindmoor Academy is a new organisation that provides group training for a year where people go through a series of workshops to heal and release emotions, get to know the real you better and support you in realizing your dreams. The end goal is personal transformation. We work with meditations, archangels, masters and elementals.
Logo and colours are attached. The fonts used are CinzelDecorative and TrajanPro.

```html
<!DOCTYPE html>
<html lang="en">
<head>
<meta charset="utf-8">
<title>Brindmoor Academy</title>
<link href="https://fonts.googleapis.com/css2?family=Cinzel:wght@400;700&family=Cinzel+Decorative:wght@400&family=Roboto:ital,wght@0,400;0,500;0,700;1,400&display=swap" rel="stylesheet">
<style>
:root{
  --purple:#7b2fb5;
  --purple-dark:#5e1e9a;
  --violet:#c45be6;
  --ink:#1d1d1d;
  --text:#555;
  --muted:#888;
  --link:#2f6fc9;
  --gold:#e8a800;
  --footer:#474747;
  --line:#e3e3e3;
}
*{box-sizing:border-box;margin:0;padding:0}
html,body{width:1200px;height:3258px;overflow:hidden}
body{position:relative;background:#fff;font-family:'Roboto',sans-serif;color:var(--text)}
.abs{position:absolute}

/* header */
.site-header{position:absolute;top:0;left:0;width:1200px;height:85px;background:#fff;z-index:5}
.brand-badge{position:absolute;left:100px;top:0;width:124px;height:120px;border-radius:0 0 62px 62px;background:#fff;display:flex;align-items:center;justify-content:center;gap:6px}
.brand-dot{width:10px;height:10px;border-radius:50%;background:var(--purple)}
.brand-name{font-family:'Cinzel',serif;font-weight:700;font-size:14px;color:var(--purple-dark);letter-spacing:.5px}
.main-nav{position:absolute;left:271px;top:33px;display:flex;gap:24px;font-size:13.5px;font-weight:500;color:var(--ink)}
.main-nav .active{color:var(--purple)}
.lang{position:absolute;left:997px;top:28px;display:flex;align-items:center;gap:14px;font-size:13.5px;font-weight:500;color:var(--ink)}
.lang-flag{width:26px;height:26px;border-radius:50%;background:linear-gradient(#c8243a 0 50%,#2b3f8c 50%)}
.caret{width:0;height:0;border-left:4px solid transparent;border-right:4px solid transparent;border-top:5px solid var(--ink)}

/* hero */
.hero-photo{position:absolute;top:85px;left:0;width:1200px;height:620px;background:linear-gradient(180deg,#a9b8bf 0%,#7e9a8a 25%,#4e7a3c 55%,#2f5a22 80%,#27401d 100%)}
.hero-wave{position:absolute;top:85px;left:0}
.hero-title{position:absolute;left:110px;top:262px;font-family:'Cinzel Decorative',serif;font-size:56px;color:#fff;letter-spacing:1px}
.hero-lead{position:absolute;left:110px;top:342px;width:500px;font-size:14.5px;line-height:24px;color:#fff}
.btn-start{position:absolute;left:110px;top:412px;width:162px;height:48px;border-radius:24px;background:var(--purple);color:#fff;font-size:13.5px;font-weight:700;display:flex;align-items:center;justify-content:center;gap:10px}
.btn-start i{width:13px;height:13px;border-radius:50%;background:#fff;position:relative}
.btn-start i::after{content:"";position:absolute;left:4px;top:3px;border-left:5px solid var(--purple);border-top:3.5px solid transparent;border-bottom:3.5px solid transparent}

/* section titles */
.section-title{position:absolute;left:0;width:1200px;text-align:center;font-family:'Cinzel',serif;font-weight:700;font-size:30px;color:var(--ink);letter-spacing:1px}

/* posts */
.post{position:absolute;width:318px}
.post-photo{height:214px}
.post-meta{position:relative;height:68px}
.post-logo{position:absolute;left:14px;top:18px;width:48px;text-align:center;font-family:'Cinzel',serif;font-weight:700;font-size:7px;color:var(--purple-dark)}
.post-logo::before{content:"";display:block;width:22px;height:22px;border-radius:50%;border:2px solid var(--purple);margin:0 auto 3px}
.post-title{position:absolute;left:82px;top:22px;font-size:14px;font-weight:700;color:var(--ink)}
.post-date{position:absolute;left:82px;top:43px;font-size:13.5px;color:var(--text)}
.post-net{position:absolute;right:10px;top:20px;width:36px;height:36px;border-radius:4px}
.net-a{background:linear-gradient(135deg,#8a3ab9,#e1306c)}
.net-b{background:#1da1f2}
.net-c{background:#1877f2}
.post-body{padding:0 15px;font-size:13.5px;line-height:21px;color:var(--text);height:78px}
.post-body a{color:var(--link);text-decoration:underline}
.post-foot{margin:0 5px;border-top:1px solid var(--line);border-bottom:1px solid var(--line);height:35px;display:flex;align-items:center;padding:0 18px;font-size:13px;color:var(--muted);gap:8px}
.post-foot svg{fill:none;stroke:#999;stroke-width:1.6}
.post-foot .gap{width:26px}
.post-foot .dl{margin-left:auto}

/* testimonials */
.testi-bg{position:absolute;top:1805px;left:0}
.testi-title{color:#fff;top:1988px}
.testi{position:absolute;top:2069px;width:319px;height:285px;background:#fff;padding:30px 25px}
.testi-avatar{position:absolute;left:30px;top:30px;width:68px;height:68px;border-radius:50%;background:linear-gradient(160deg,#d9c2b0,#8a6a58)}
.testi-name{position:absolute;left:122px;top:48px;font-size:15px;font-weight:700;color:var(--ink)}
.testi-role{position:absolute;left:122px;top:68px;font-size:14px;color:var(--text)}
.testi-text{position:absolute;left:25px;top:135px;width:275px;font-size:13.5px;line-height:23px;font-style:italic;color:var(--text)}
.testi-stars{position:absolute;left:25px;top:236px;color:var(--gold);font-size:15px;letter-spacing:1px}
.testi-quote{position:absolute;right:26px;top:226px;font-family:Georgia,serif;font-weight:700;font-size:44px;line-height:44px;color:var(--purple)}

/* newsletter */
.news-title{position:absolute;left:114px;top:2628px;font-family:'Cinzel Decorative',serif;font-size:27px;color:var(--ink)}
.news-lead{position:absolute;left:114px;top:2676px;width:340px;font-size:14px;line-height:23px;color:var(--text)}
.news-form{position:absolute;left:532px;top:2648px;width:553px;height:50px;box-shadow:0 2px 8px rgba(0,0,0,.12);background:#fff;display:flex}
.news-form span{flex:1;padding:16px 25px;font-size:14px;color:#666}
.news-form b{width:152px;background:var(--purple);color:#fff;font-size:13.5px;display:flex;align-items:center;justify-content:center}

/* footer */
.footer-wave{position:absolute;top:2755px;left:0}
.footer-body{position:absolute;top:2900px;left:0;width:1200px;height:358px;background:var(--footer)}
.footer-brand{position:absolute;left:150px;top:3080px;display:flex;align-items:center;gap:10px;font-family:'Cinzel',serif;font-weight:700;font-size:24px;color:#fff}
.footer-brand i{width:14px;height:14px;border-radius:50%;background:#fff}
.foot-col{position:absolute;top:2960px;color:#fff}
.foot-col h4{font-size:13.5px;font-weight:700;margin-bottom:16px}
.foot-col li{list-style:none;font-size:14px;line-height:34.5px;padding-left:26px;position:relative}
.foot-col li::before{content:"»";position:absolute;left:0;font-size:14px}
.contact-row{display:flex;align-items:center;gap:20px;height:50px;margin-bottom:12px;font-size:14px;line-height:24px}
.contact-row .ring{width:36px;height:36px;border:1.5px solid #fff;border-radius:50%;display:flex;align-items:center;justify-content:center;flex:none}
.contact-row svg{fill:none;stroke:#fff;stroke-width:1.7}
.footer-rule{position:absolute;left:113px;top:3193px;width:975px;border-top:1px solid #8a8a8a}
.copyright{position:absolute;left:114px;top:3217px;font-size:14px;color:#fff}
.chat-bubble{position:absolute;left:1036px;top:3211px;width:36px;height:36px;border-radius:50%;background:#3b8cf5}
</style>
</head>
<body>

<header class="site-header">
  <div class="brand-badge"><i class="brand-dot"></i><span class="brand-name">BRINDMOOR</span></div>
  <nav class="main-nav">
    <span class="active">HOME</span><span>ABOUT US</span><span>OUR ACADEMY</span><span>VIRELTONES</span><span>PERSONAL VIRELTONES</span><span>FROM METATRON</span>
  </nav>
  <div class="lang"><span class="lang-flag"></span><span>ENG</span><span class="caret"></span></div>
</header>

<section class="hero">
  <div class="hero-photo" role="img" aria-label="Woman meditating with raised hands above a misty green valley"></div>
  <svg class="hero-wave" width="1200" height="620" viewBox="0 0 1200 620">
    <defs><linearGradient id="band" x1="0" x2="1"><stop offset="0" stop-color="#5e1e9a"/><stop offset="1" stop-color="#c45be6"/></linearGradient></defs>
    <path d="M0,490 C110,600 320,620 520,585 C600,570 585,625 680,612 C790,596 850,460 960,505 C1050,545 1120,535 1200,505 L1200,620 L0,620Z" fill="url(#band)"/>
    <path d="M0,522 C120,625 330,645 525,612 C605,598 595,650 685,638 C800,620 855,490 965,532 C1055,568 1120,570 1200,545 L1200,620 L0,620Z" fill="#fff"/>
  </svg>
  <h1 class="hero-title">BRINDMOOR</h1>
  <p class="hero-lead">Lorem ipsum dolor sit amet, consectetur adipiscing elit, sed do eiusmod tempor incididunt ut labore et dolore magna aliqua.</p>
  <div class="btn-start">GET STARTED <i></i></div>
</section>

<h2 class="section-title" style="top:772px">SOCIAL MEDIA POSTS</h2>

<!-- posts -->
<article class="post" style="left:99px;top:865px">
  <div class="post-photo" role="img" aria-label="Woman meditating cross-legged on a wooden floor" style="background:linear-gradient(135deg,#e9e4dc,#b9a994)"></div>
  <div class="post-meta"><div class="post-logo">BRINDMOOR</div><div class="post-title">SED UT PERSPICIATIS</div><div class="post-date">20 May 2021</div><div class="post-net net-a"></div></div>
  <p class="post-body"><a>At vero eos</a> et accusamus et iusto dignissimos ducimus qui blanditiis praesentiumvoluptatum deleniti atque corrupti quos dolor</p>
  <div class="post-foot"><svg width="14" height="13"><path d="M7 12 1.5 6.5A3 3 0 0 1 7 2.5a3 3 0 0 1 5.5 4Z"/></svg>201<span class="gap"></span><svg width="15" height="12"><path d="M9 1l5 4.5L9 10V7C5 7 2.5 8 1 11c.5-4.5 3-7 8-7.5Z" fill="#999" stroke="none"/></svg>25<svg class="dl" width="14" height="13"><path d="M7 1v7M4 5.5 7 8.5l3-3M1.5 10v2h11v-2"/></svg></div>
</article>
<article class="post" style="left:441px;top:865px">
  <div class="post-photo" role="img" aria-label="Woman meditating in a bright bedroom" style="background:linear-gradient(135deg,#ece8e4,#bfb5ad)"></div>
  <div class="post-meta"><div class="post-logo">BRINDMOOR</div><div class="post-title">SED UT PERSPICIATIS</div><div class="post-date">20 May 2021</div><div class="post-net net-b"></div></div>
  <p class="post-body"><a>At vero eos</a> et accusamus et iusto dignissimos ducimus qui blanditiis praesentiumvoluptatum deleniti atque corrupti quos dolor</p>
  <div class="post-foot"><svg width="14" height="13"><path d="M7 12 1.5 6.5A3 3 0 0 1 7 2.5a3 3 0 0 1 5.5 4Z"/></svg>201<span class="gap"></span><svg width="15" height="12"><path d="M9 1l5 4.5L9 10V7C5 7 2.5 8 1 11c.5-4.5 3-7 8-7.5Z" fill="#999" stroke="none"/></svg>25<svg class="dl" width="14" height="13"><path d="M7 1v7M4 5.5 7 8.5l3-3M1.5 10v2h11v-2"/></svg></div>
</article>
<article class="post" style="left:784px;top:865px">
  <div class="post-photo" role="img" aria-label="Couple meditating together in a living room" style="background:linear-gradient(135deg,#9a938c,#3c3834)"></div>
  <div class="post-meta"><div class="post-logo">BRINDMOOR</div><div class="post-title">SED UT PERSPICIATIS</div><div class="post-date">20 May 2021</div><div class="post-net net-c"></div></div>
  <p class="post-body"><a>At vero eos</a> et accusamus et iusto dignissimos ducimus qui blanditiis praesentiumvoluptatum deleniti atque corrupti quos dolor</p>
  <div class="post-foot"><svg width="14" height="13"><path d="M7 12 1.5 6.5A3 3 0 0 1 7 2.5a3 3 0 0 1 5.5 4Z"/></svg>201<span class="gap"></span><svg width="15" height="12"><path d="M9 1l5 4.5L9 10V7C5 7 2.5 8 1 11c.5-4.5 3-7 8-7.5Z" fill="#999" stroke="none"/></svg>25<svg class="dl" width="14" height="13"><path d="M7 1v7M4 5.5 7 8.5l3-3M1.5 10v2h11v-2"/></svg></div>
</article>
<article class="post" style="left:99px;top:1319px">
  <div class="post-photo" role="img" aria-label="Man meditating with earphones on a yoga mat" style="background:linear-gradient(135deg,#e4e1dc,#9d9489)"></div>
  <div class="post-meta"><div class="post-logo">BRINDMOOR</div><div class="post-title">SED UT PERSPICIATIS</div><div class="post-date">20 May 2021</div><div class="post-net net-a"></div></div>
  <p class="post-body"><a>At vero eos</a> et accusamus et iusto dignissimos ducimus qui blanditiis praesentiumvoluptatum deleniti atque corrupti quos dolor</p>
  <div class="post-foot"><svg width="14" height="13"><path d="M7 12 1.5 6.5A3 3 0 0 1 7 2.5a3 3 0 0 1 5.5 4Z"/></svg>201<span class="gap"></span><svg width="15" height="12"><path d="M9 1l5 4.5L9 10V7C5 7 2.5 8 1 11c.5-4.5 3-7 8-7.5Z" fill="#999" stroke="none"/></svg>25<svg class="dl" width="14" height="13"><path d="M7 1v7M4 5.5 7 8.5l3-3M1.5 10v2h11v-2"/></svg></div>
</article>
<article class="post" style="left:441px;top:1319px">
  <div class="post-photo" role="img" aria-label="Woman meditating in a white studio" style="background:linear-gradient(135deg,#f1f0ee,#c9c2bd)"></div>
  <div class="post-meta"><div class="post-logo">BRINDMOOR</div><div class="post-title">SED UT PERSPICIATIS</div><div class="post-date">20 May 2021</div><div class="post-net net-b"></div></div>
  <p class="post-body"><a>At vero eos</a> et accusamus et iusto dignissimos ducimus qui blanditiis praesentiumvoluptatum deleniti atque corrupti quos dolor</p>
  <div class="post-foot"><svg width="14" height="13"><path d="M7 12 1.5 6.5A3 3 0 0 1 7 2.5a3 3 0 0 1 5.5 4Z"/></svg>201<span class="gap"></span><svg width="15" height="12"><path d="M9 1l5 4.5L9 10V7C5 7 2.5 8 1 11c.5-4.5 3-7 8-7.5Z" fill="#999" stroke="none"/></svg>25<svg class="dl" width="14" height="13"><path d="M7 1v7M4 5.5 7 8.5l3-3M1.5 10v2h11v-2"/></svg></div>
</article>
<article class="post" style="left:784px;top:1319px">
  <div class="post-photo" role="img" aria-label="Smiling woman meditating on a beach" style="background:linear-gradient(180deg,#d6dde2,#b9c3c8 55%,#d9cbb8)"></div>
  <div class="post-meta"><div class="post-logo">BRINDMOOR</div><div class="post-title">SED UT PERSPICIATIS</div><div class="post-date">20 May 2021</div><div class="post-net net-c"></div></div>
  <p class="post-body"><a>At vero eos</a> et accusamus et iusto dignissimos ducimus qui blanditiis praesentiumvoluptatum deleniti atque corrupti quos dolor</p>
  <div class="post-foot"><svg width="14" height="13"><path d="M7 12 1.5 6.5A3 3 0 0 1 7 2.5a3 3 0 0 1 5.5 4Z"/></svg>201<span class="gap"></span><svg width="15" height="12"><path d="M9 1l5 4.5L9 10V7C5 7 2.5 8 1 11c.5-4.5 3-7 8-7.5Z" fill="#999" stroke="none"/></svg>25<svg class="dl" width="14" height="13"><path d="M7 1v7M4 5.5 7 8.5l3-3M1.5 10v2h11v-2"/></svg></div>
</article>

<!-- testimonials -->
<svg class="testi-bg" width="1200" height="760" viewBox="0 0 1200 760" role="img" aria-label="Stacked balance stones on a beach at sunset">
  <defs><linearGradient id="dusk" x1="0" y1="0" x2="0" y2="1"><stop offset="0" stop-color="#b593b4"/><stop offset=".35" stop-color="#c9a3a9"/><stop offset=".6" stop-color="#7b5f82"/><stop offset="1" stop-color="#4e3a5c"/></linearGradient></defs>
  <path d="M0,75 C100,120 220,150 300,110 C390,60 480,-10 600,60 C640,90 620,20 760,30 C900,45 1000,10 1080,0 C1140,-5 1180,20 1200,55 L1200,680 C1140,640 1060,720 980,660 C900,600 800,640 720,700 C620,760 540,730 430,735 C280,745 140,720 0,690Z" fill="url(#dusk)"/>
</svg>
<h2 class="section-title testi-title">TESTIMONIALS</h2>

<div class="testi" style="left:107px">
  <div class="testi-avatar" role="img" aria-label="Customer portrait"></div>
  <div class="testi-name">MARA ELLISON</div><div class="testi-role">Businessman</div>
  <p class="testi-text">Sed ut perspiciatis unde omnis iste natus error sit voluptatem accusanti doloremque laudantium, totam rem aperiam, eaque ipsa quae ab illo inventore</p>
  <div class="testi-stars">★★★★★</div><div class="testi-quote">”</div>
</div>
<div class="testi" style="left:440px">
  <div class="testi-avatar" role="img" aria-label="Customer portrait"></div>
  <div class="testi-name">MARA ELLISON</div><div class="testi-role">Businessman</div>
  <p class="testi-text">Sed ut perspiciatis unde omnis iste natus error sit voluptatem accusanti doloremque laudantium, totam rem aperiam, eaque ipsa quae ab illo inventore</p>
  <div class="testi-stars">★★★★★</div><div class="testi-quote">”</div>
</div>
<div class="testi" style="left:773px">
  <div class="testi-avatar" role="img" aria-label="Customer portrait"></div>
  <div class="testi-name">MARA ELLISON</div><div class="testi-role">Businessman</div>
  <p class="testi-text">Sed ut perspiciatis unde omnis iste natus error sit voluptatem accusanti doloremque laudantium, totam rem aperiam, eaque ipsa quae ab illo inventore</p>
  <div class="testi-stars">★★★★★</div><div class="testi-quote">”</div>
</div>

<!-- newsletter -->
<h2 class="news-title">Sign Up For Newsletter</h2>
<p class="news-lead">Sed ut perspiciatis unde omnis iste natus error sit voluptatem accusantium dolor.</p>
<div class="news-form"><span>Email Address</span><b>SUBSCRIBE</b></div>

<!-- footer -->
<svg class="footer-wave" width="1200" height="150" viewBox="0 0 1200 150">
  <defs><linearGradient id="band2" x1="0" x2="1"><stop offset="0" stop-color="#6a22a8"/><stop offset="1" stop-color="#d36ef0"/></linearGradient></defs>
  <path d="M0,90 C90,70 200,70 260,110 C310,150 360,110 470,70 C560,40 590,80 620,80 C720,75 820,30 900,15 C990,0 1080,-5 1200,25 L1200,150 L0,150Z" fill="url(#band2)"/>
  <path d="M0,118 C90,98 200,95 262,135 C315,170 370,135 475,100 C565,70 600,115 630,112 C730,105 830,60 910,48 C1000,35 1090,45 1200,75 L1200,150 L0,150Z" fill="var(--footer)"/>
</svg>
<footer class="footer-body"></footer>
<div class="footer-brand"><i></i>BRINDMOOR</div>

<div class="foot-col" style="left:421px">
  <h4>QUICK LINKS</h4>
  <ul><li>Home</li><li>About Us</li><li>Vireltones</li><li>Personal Vireltones</li><li>From Metatron</li></ul>
</div>
<div class="foot-col" style="left:668px">
  <h4>OTHER LINKS</h4>
  <ul><li>Terms Of Use</li><li>Privacy Policy</li><li>Help Service</li><li>Contact Us</li><li>FAQ</li></ul>
</div>
<div class="foot-col" style="left:874px">
  <h4>CONTACT US</h4>
  <div class="contact-row"><span class="ring"><svg width="14" height="18"><path d="M7 17S1.5 10.5 1.5 6.5a5.5 5.5 0 0 1 11 0C12.5 10.5 7 17 7 17Z"/><circle cx="7" cy="6.5" r="2"/></svg></span><span>48 Harrow Lane,<br>Reykjavik</span></div>
  <div class="contact-row"><span class="ring"><svg width="16" height="12"><rect x="1" y="1" width="14" height="10" rx="1.5"/><path d="M1.5 2 8 7l6.5-5"/></svg></span><span>info@brindmoor.is</span></div>
  <div class="contact-row"><span class="ring"><svg width="16" height="16"><path d="M4 1.5 6 5 4.5 6.5a8 8 0 0 0 5 5L11 10l3.5 2-1 2.5C8 15 1 8 1.5 2.5Z" fill="#fff" stroke="none"/></svg></span><span>1 555 014 2290</span></div>
</div>

<div class="footer-rule"></div>
<p class="copyright">© 2021 Brindmoor. All Rights Reserved</p>
<div class="chat-bubble"></div>

</body>
</html>
```